Business Card Design Project

We need a business card design for our company kV7 s.r.o. The company is based in Slovakia and selling massage, yoga and meditation accessories online and offline. At the place where the offices are, we have a yoga studio, massage room, show room and shop as well. We will give the business card for customers who visit our shop or show room personally and for the new suppliers of demanded products we are visiting in the future.
I would like to have:
- small logo and datas on one side
- big logo and our main e-shops on the other side:
- www.pohodanoviny.sk
- www.relaxbrodeky.cz
Datas:
Peter Hulka, MSc. / CEO
kV7 s.r.o.
Brezovanská 742/3
931 05 Lipová Dolina
Slovak republic (Slovakia)
Office tel.: +421 (0) 947 618 204
Private tel.: +421 (0) 907 251 836
E-mail: info@kv7example.sk
Web: www.kv7example.sk
It is up to you if you use graphics emphasizing our profile or leave it simple and modern without pics. Looking forward to receiving your designs! Thank You!
Industry/Entity Type
Massage
Colors
Designer to choose colors to be used in the design.
Look and feel
Each slider illustrates characteristics of the customer's brand and the style your logo design should communicate.

```html
<!DOCTYPE html>
<html lang="en">
<head>
<meta charset="utf-8">
<title>KV SEDEM – Business Card</title>
<link rel="stylesheet" href="https://fonts.googleapis.com/css2?family=Exo+2:wght@400;600;700&display=swap">
<style>
  :root {
    --canvas: #ececec;
    --brand-orange: #f07a0c;
    --slate: #4a5262;
    --white: #ffffff;
    --glow-orange: rgba(255, 210, 160, 0.35);
    --glow-slate: rgba(140, 148, 162, 0.35);
  }
  * { box-sizing: border-box; margin: 0; padding: 0; }
  html, body {
    width: 1200px; height: 900px; overflow: hidden;
    background: var(--canvas);
    font-family: "Exo 2", Arial, sans-serif;
  }
  .stage { position: relative; width: 1200px; height: 900px; }

  .card {
    position: absolute;
    width: 540px; height: 300px;
    border-radius: 3px;
    box-shadow: 0 6px 18px rgba(0,0,0,0.15);
    overflow: hidden;
  }

  /* Front: large name and e-shops */
  .card--front { left: 560px; top: 90px; background: var(--brand-orange); }
  .card--front .glow {
    position: absolute; left: 30px; top: 30px; width: 330px; height: 240px;
    background: radial-gradient(ellipse at 60% 45%, var(--glow-orange), transparent 70%);
  }
  .brand-large {
    position: absolute; left: 0; right: 0; top: 78px;
    text-align: center;
    font-size: 76px; font-weight: 700; line-height: 1;
    color: var(--white); letter-spacing: 2px;
  }
  .eshops {
    position: absolute; right: 100px; top: 196px;
    text-align: right; color: var(--white);
    font-size: 19px; line-height: 1.2; font-weight: 400;
  }
  .eshops strong { font-weight: 700; }

  /* Back: contact details */
  .card--back { left: 100px; top: 470px; background: var(--slate); }
  .card--back .glow {
    position: absolute; left: 250px; top: 60px; width: 260px; height: 200px;
    background: radial-gradient(ellipse at 50% 40%, var(--glow-slate), transparent 70%);
  }
  .brand-small {
    position: absolute; right: 40px; top: 40px;
    font-size: 30px; font-weight: 700; line-height: 1;
    color: var(--white); letter-spacing: 1px;
  }
  .contact {
    position: absolute; left: 40px; top: 106px;
    color: var(--white); font-size: 15px; line-height: 1.2;
  }
  .contact .person { font-size: 19px; font-weight: 600; margin-bottom: 10px; }
  .contact .person .degree { font-weight: 400; }
  .contact .person .role { color: var(--brand-orange); font-weight: 400; }
  .contact .company { color: var(--brand-orange); font-weight: 700; }
  .contact .address { margin-bottom: 10px; }
  .contact .label { color: var(--brand-orange); font-weight: 700; }
</style>
</head>
<body>
<main class="stage">

  <section class="card card--front" aria-label="Business card front">
    <div class="glow" role="img" aria-label="Soft decorative background pattern"></div>
    <p class="brand-large">KV SEDEM</p>
    <p class="eshops">
      www.<strong>pohodanoviny</strong>.sk<br>
      www.<strong>relaxbrodeky</strong>.cz
    </p>
  </section>

  <section class="card card--back" aria-label="Business card back">
    <div class="glow" role="img" aria-label="Soft decorative background pattern"></div>
    <p class="brand-small">KV SEDEM</p>
    <div class="contact">
      <p class="person">Peter Hulka, <span class="degree">MSc.</span> | <span class="role">CEO</span></p>
      <div class="address">
        <p class="company">kV7 s.r.o.</p>
        <p>Brezovanská 742/3</p>
        <p>931 05 Lipová Dolina</p>
        <p>Slovak republic (Slovakia)</p>
      </div>
      <p><span class="label">Office tel.:</span> +421 (0) 947 618 204</p>
      <p><span class="label">Private tel.:</span> +421 (0) 907 251 836</p>
      <p><span class="label">E-mail:</span> info@kv7example.sk</p>
      <p><span class="label">Web:</span> www.kv7example.sk</p>
    </div>
  </section>

</main>
</body>
</html>
```